Wedding Decor and Entertianment business card

Company - We run a weddings and events company called Amber Fern, we provide most entertainment and decor services to our customers.

Initial idea is ....
A simple business card with logo on the front, this will be spot varnish. On a matt black background.
The reverse will be simple contact information.

But happy to try things outside of the box and would welcome some crazy ideas.

Target Market(s)

wedding couples - 21 - 40
High end wedding venues.

Industry/Entity Type

Wedding

Contact Information for Business Card

01742 918 263
amberfern.co.uk
rupert@amberfern.co.uk
or
eleanor@amberfern.co.uk

Requirements
Nice to have
• black matt background with spot varnish logo on the front.

```html
<!DOCTYPE html>
<html lang="en">
<head>
<meta charset="utf-8">
<title>Amber Fern — Business Card</title>
<link rel="stylesheet" href="https://fonts.googleapis.com/css2?family=Jost:wght@300;400;500&display=swap">
<style>
  :root {
    --backdrop: #3b3431;
    --card-black: #141414;
    --card-edge: #0b0b0b;
    --varnish: #d9d9dc;
    --plum: #8d5e8f;
    --plum-soft: rgba(141, 94, 143, 0.55);
    --ink-light: #e4e4e4;
  }
  * { box-sizing: border-box; margin: 0; padding: 0; }
  html, body {
    width: 1200px;
    height: 787px;
    overflow: hidden;
    background: var(--backdrop);
    font-family: "Jost", "Futura", sans-serif;
  }
  .canvas {
    position: relative;
    width: 1200px;
    height: 787px;
    display: flex;
    align-items: center;
    justify-content: center;
    gap: 60px;
  }
  .card {
    position: relative;
    width: 520px;
    height: 320px;
    background: var(--card-black);
    border: 1px solid var(--card-edge);
    box-shadow: 0 10px 30px rgba(0, 0, 0, 0.35);
  }

  /* Front: spot-varnish wordmark */
  .card-front {
    display: flex;
    align-items: center;
    justify-content: center;
  }
  .front-mark {
    display: flex;
    align-items: center;
    gap: 22px;
  }
  .front-mark .mark-dot {
    width: 26px;
    height: 26px;
    border-radius: 50%;
    background: var(--varnish);
  }
  .front-mark .wordmark {
    font-weight: 300;
    font-size: 30px;
    letter-spacing: 0.42em;
    color: var(--varnish);
    text-transform: uppercase;
  }

  /* Back: contact details */
  .card-back {
    display: flex;
    flex-direction: column;
    align-items: center;
    padding-top: 62px;
  }
  .back-mark {
    display: flex;
    align-items: center;
    gap: 12px;
  }
  .back-mark .mark-dot {
    width: 16px;
    height: 16px;
    border-radius: 50%;
    background: var(--plum);
  }
  .back-mark .wordmark {
    font-weight: 400;
    font-size: 22px;
    letter-spacing: 0.22em;
    color: var(--plum);
    text-transform: uppercase;
  }
  .divider {
    width: 440px;
    height: 1px;
    margin: 22px 0 18px;
    background: linear-gradient(to right, transparent, var(--plum-soft) 20%, var(--plum) 50%, var(--plum-soft) 80%, transparent);
  }
  .contact {
    text-align: center;
    color: var(--ink-light);
    font-size: 18px;
    font-weight: 300;
    line-height: 1.35;
  }
  .contact .person {
    color: var(--plum);
    font-weight: 500;
    font-size: 21px;
    letter-spacing: 0.06em;
    text-transform: uppercase;
    margin-bottom: 4px;
  }
  .contact .label {
    color: var(--plum);
    font-weight: 500;
  }
</style>
</head>
<body>
  <main class="canvas">
    <section class="card card-front" aria-label="Card front">
      <div class="front-mark">
        <span class="mark-dot"></span>
        <span class="wordmark">Amber Fern</span>
      </div>
    </section>

    <section class="card card-back" aria-label="Card back">
      <div class="back-mark">
        <span class="mark-dot"></span>
        <span class="wordmark">Amber Fern</span>
      </div>
      <div class="divider"></div>
      <address class="contact" style="font-style: normal;">
        <p class="person">Rupert Hale</p>
        <p><span class="label">Phone</span> : 01742 918 263</p>
        <p>rupert@amberfern.co.uk</p>
        <p>www.amberfern.co.uk</p>
      </address>
    </section>
  </main>
</body>
</html>
```